Medical Billing Company needs Trifold Brochure Design

We do medical billing and consulting for all types of medical services including hospitals, clinics, physical therapy, mental health, and all other physician specialties. We want to attract new clients from all areas. This is what we have listed on our Brindlepost page: Qorvant Billing and Consulting offers 128 years of combined medical billing, coding, credentialing, auditing, and practice management experience. Integrity, reliability, dedication, and open communication are the cornerstones of our foundation. We strive to create meaningful relationships with our clients so they may focus on what they do best, and allow us to handle the rest.

We understand the changes occurring in our healthcare system. Reimbursement is decreasing, expenses are increasing, and the dedication and tenacity to collect every dollar due from the carriers is vital to the financial health of the hospital or practitioner.

Target Market(s)

Physicians, hospitals and any other providers in the medical field such as durable medical equipment suppliers and mid-level providers

Font styles to use
Sans Serif

Colors

Designer to choose colors to be used in the design.

Requirements
Must have
• Specifics list of services we offer. List attached.

```html
<!DOCTYPE html>
<html lang="en">
<head>
<meta charset="utf-8">
<title>Qorvant Billing and Consulting – Trifold Brochure</title>
<link rel="stylesheet" href="https://fonts.googleapis.com/css2?family=Roboto:wght@400;500;700&family=Roboto+Condensed:wght@400;700&display=swap">
<style>
:root{
  --bg:#dcdde0;
  --navy:#0f2d52;
  --blue:#1f6ea6;
  --blue-deep:#143a66;
  --green:#3d9a3a;
  --green-dark:#2f7f2e;
  --ink:#1b1b1b;
  --title-blue:#1d6fa8;
  --sky-top:#d5e9f6;
  --sky-bot:#a9d5f0;
  --list-ink:#1d4f80;
  --white:#ffffff;
}
*{margin:0;padding:0;box-sizing:border-box}
html,body{width:1200px;height:1200px;overflow:hidden}
body{background:var(--bg);font-family:"Roboto",sans-serif;position:relative}
.sheet{position:absolute;width:711px;height:552px;overflow:hidden;box-shadow:0 10px 18px rgba(0,0,0,.25)}
.sheet--outside{left:55px;top:46px;background:var(--white)}
.sheet--inside{left:426px;top:614px;background:linear-gradient(180deg,var(--sky-top),var(--sky-bot))}
.panel{position:absolute;top:0;height:100%}
.band{position:absolute;left:0;width:100%}
/* outside: about */
.about{left:0;width:240px}
.about__title{position:absolute;left:25px;top:34px;font-size:31px;font-weight:400;color:var(--title-blue)}
.about__body{position:absolute;left:25px;top:80px;width:194px;font-size:8.6px;line-height:11.7px;color:var(--ink);text-align:justify}
.about__body p{margin-bottom:11.7px}
.about__photo-frame{position:absolute;left:20px;top:343px;width:202px;height:179px;background:var(--white);border-radius:4px;z-index:2}
.about__photo{position:absolute;left:4px;top:4px;right:4px;bottom:4px;background:linear-gradient(135deg,#3b4f6e,#c9d3df 45%,#6d7f99 70%,#e6ebf1)}
/* outside: pitch */
.pitch{left:240px;width:236px;background:linear-gradient(180deg,var(--blue) 0%,var(--blue-deep) 55%,var(--navy) 80%)}
.pitch__headline{position:absolute;left:19px;top:34px;font-family:"Roboto Condensed",sans-serif;font-weight:700;color:var(--white);font-size:31px;line-height:29px}
.pitch__headline span{display:block;font-size:19px;line-height:24px;margin-top:3px}
.pitch__text{position:absolute;left:19px;top:125px;width:202px;font-family:"Roboto Condensed",sans-serif;font-weight:700;color:var(--white);font-size:9.2px;line-height:12px}
.pitch__text p{margin-bottom:12px}
.quote{position:absolute;left:20px;top:253px;width:190px;height:98px;border-radius:14px;background:rgba(20,50,95,.75);padding:14px 10px 0 17px;font-family:"Roboto Condensed",sans-serif;font-weight:700;color:var(--white);font-size:7.2px;line-height:10px}
.quote__mark{position:absolute;left:9px;top:3px;font-size:24px;color:#6e89ad;font-family:"Roboto",sans-serif}
.quote__text{padding-left:16px}
.quote__by{text-align:right;margin-top:6px;padding-right:10px}
.contact{position:absolute;left:0;top:441px;width:100%;text-align:center;font-family:"Roboto Condensed",sans-serif;font-weight:700;color:var(--white);font-size:10.4px;line-height:13.5px}
.contact__gap{height:12px}
.contact__web{margin-top:14px}
/* outside: cover */
.cover{left:476px;width:235px;background:var(--white)}
.brand{position:absolute;left:30px;top:46px;display:flex;align-items:center;gap:8px}
.brand__square{width:30px;height:30px;background:var(--green)}
.brand__name{font-size:26px;font-weight:700;color:var(--blue-deep);line-height:1}
.brand__sub{position:absolute;left:68px;top:78px;font-size:8.5px;font-weight:500;color:var(--green-dark);letter-spacing:.4px}
.cover__photo{position:absolute;left:0;top:112px;width:100%;height:300px;background:linear-gradient(180deg,#f4f6f8,#e3e9ee 60%,#d8e0e6)}
.cover__tag{position:absolute;left:0;top:437px;width:100%;text-align:center;font-family:"Roboto Condensed",sans-serif;font-weight:700;color:var(--navy);font-size:15.5px;line-height:20px;z-index:2}
.cover__sub{position:absolute;left:0;top:484px;width:100%;text-align:center;font-family:"Roboto Condensed",sans-serif;font-weight:700;color:var(--white);font-size:10.4px;line-height:14px;z-index:2}
.cover__web{position:absolute;left:0;top:522px;width:100%;text-align:center;font-family:"Roboto Condensed",sans-serif;font-weight:700;color:var(--white);font-size:10.4px;z-index:2}
.fold{position:absolute;top:0;width:1px;height:100%;background:rgba(0,0,0,.08)}
/* inside */
.hero{position:absolute;left:0;top:0;width:100%;height:262px;background:linear-gradient(90deg,#e4ecf4 0%,#aebed2 25%,#7e98b8 55%,#3f5f8a 72%,#2a4a78 100%)}
.hero__headline{position:absolute;left:494px;top:38px;width:210px;font-weight:700;color:var(--white);font-size:27px;line-height:26px}
.hero__cta{position:absolute;left:494px;top:157px;color:var(--white);font-size:12px;font-weight:500}
.hero__phone{position:absolute;left:494px;top:175px;color:var(--white);font-size:21px;font-weight:700}
.services{position:absolute;top:270px;width:205px;list-style:none}
.services--a{left:27px}.services--b{left:262px}.services--c{left:489px;width:215px}
.services li{display:flex;align-items:center;gap:10px;height:52px;border-bottom:1px solid rgba(29,79,128,.25);font-size:13.8px;line-height:17.5px;color:var(--list-ink);text-transform:uppercase}
.services li:last-child{border-bottom:none}
.tick{flex:0 0 21px;width:21px;height:18px}
</style>
</head>
<body>

<section class="sheet sheet--outside" aria-label="Brochure outside">
  <div class="panel about">
    <h2 class="about__title">About Us</h2>
    <div class="about__body">
      <p>We do medical billing and consulting for all types of medical services including hospitals, clinics, physical therapy, mental health, and all other physician specialties.</p>
      <p>Qorvant Billing and Consulting offers 128 years of combined medical billing, coding, credentialing, auditing, and practice management experience. Integrity, reliability, dedication, and open communication are the cornerstones of our foundation. We strive to create meaningful relationships with our clients so they may focus on what they do best, and allow us to handle the rest.</p>
      <p>We understand the changes occurring in our healthcare system. Reimbursement is decreasing, expenses are increasing, and the dedication and tenacity to collect every dollar due from the carriers is vital to the financial health of the hospital or practitioner.</p>
    </div>
    <svg class="band" style="top:415px;height:137px" viewBox="0 0 240 137" preserveAspectRatio="none" aria-hidden="true">
      <path d="M0 20 Q120 0 240 12 L240 137 L0 137 Z" fill="var(--green)"/>
    </svg>
    <div class="about__photo-frame"><div class="about__photo" role="img" aria-label="Photo of rows of patient record files"></div></div>
  </div>

  <div class="panel pitch">
    <h1 class="pitch__headline">FEWER<br>HEADACHES,<span>MORE PROFITABILITY</span></h1>
    <div class="pitch__text">
      <p>In this age of declining Reimbursement, there is no room for errors. Incorrect coding, can mean revenue that is lost forever. Stay in the Black with our professional billing services. The most competitive rates in the industry.</p>
      <p>We work in your system or ours. We have a clean claim rate of 98.7 percent and, we don't get paid until YOU get paid.</p>
    </div>
    <blockquote class="quote">
      <span class="quote__mark">&ldquo;</span>
      <p class="quote__text">On another note, I know I don't say it often enough but Thank you both for all you are doing; your leadership, your patience, your professionalism and your kindness just to name a few. I appreciate you more than you know.&rdquo;</p>
      <p class="quote__by">T.L. Harlow</p>
    </blockquote>
    <svg class="band" style="top:355px;height:197px" viewBox="0 0 236 197" preserveAspectRatio="none" aria-hidden="true">
      <path d="M0 45 Q120 20 200 5 Q110 35 0 50 Z" fill="var(--white)"/>
      <path d="M0 62 Q130 28 236 33 L236 197 L0 197 Z" fill="var(--white)"/>
      <path d="M0 82 Q130 48 236 48 L236 197 L0 197 Z" fill="var(--green)"/>
    </svg>
    <address class="contact" style="font-style:normal">
      <div>48 LARKSPUR RIDGE CT.</div>
      <div>MESA ALTA, NM 88100</div>
      <div class="contact__gap"></div>
      <div>555.014.2270 &nbsp;TEL</div>
      <div>555.014.2291 FAX</div>
      <div class="contact__web">WWW.QORVANTBILLING.COM</div>
    </address>
  </div>

  <div class="panel cover">
    <div class="brand"><span class="brand__square"></span><span class="brand__name">Qorvant</span></div>
    <div class="brand__sub">BILLING &amp; CONSULTING</div>
    <div class="cover__photo" role="img" aria-label="Photo of two smiling female doctors reviewing a clipboard"></div>
    <svg class="band" style="top:380px;height:172px" viewBox="0 0 235 172" preserveAspectRatio="none" aria-hidden="true">
      <path d="M0 12 Q120 5 235 10 L235 172 L0 172 Z" fill="var(--green)"/>
      <path d="M45 22 Q150 8 235 25 L235 21 Q150 4 45 22 Z" fill="var(--white)"/>
    </svg>
    <div class="cover__tag">THE BEST MEDICINE FOR<br>A BROKEN BILLING CYCLE</div>
    <div class="cover__sub">QUICK COST EFFECTIVE<br>EFFICIENT BILLING SOLUTIONS</div>
    <div class="cover__web">WWW.QORVANTBILLING.COM</div>
  </div>
  <span class="fold" style="left:240px"></span>
  <span class="fold" style="left:476px"></span>
</section>

<section class="sheet sheet--inside" aria-label="Brochure inside">
  <div class="hero" role="img" aria-label="Photo of a smiling doctor in a clinic with nurses attending a patient"></div>
  <svg class="band" style="top:220px;height:60px" viewBox="0 0 711 60" preserveAspectRatio="none" aria-hidden="true">
    <path d="M0 40 Q250 70 420 35 Q560 8 711 15 L711 0 L0 0 Z" fill="none"/>
    <path d="M0 42 Q260 66 430 34 Q570 10 711 16 L711 48 Q570 38 430 46 Q260 62 0 52 Z" fill="var(--navy)"/>
    <path d="M0 52 Q260 62 430 46 Q570 38 711 48 L711 60 L0 60 Z" fill="var(--sky-top)"/>
  </svg>
  <h2 class="hero__headline">Making medical billing an easy task with our services</h2>
  <p class="hero__cta">Call now to find out how:</p>
  <p class="hero__phone">555-014-2270</p>

  <svg width="0" height="0" style="position:absolute" aria-hidden="true">
    <symbol id="tick" viewBox="0 0 21 18"><path d="M1 10 L5 7 L8.5 12 L17 1 L20.5 4 L9 17 Z" fill="var(--navy)"/></symbol>
  </svg>

  <ul class="services services--a">
    <li><svg class="tick"><use href="#tick"/></svg>Electronic &amp;<br>Paper Claims</li>
    <li><svg class="tick"><use href="#tick"/></svg>Insurance<br>Follow Ups</li>
    <li><svg class="tick"><use href="#tick"/></svg>Monthly<br>Patient Billing</li>
    <li><svg class="tick"><use href="#tick"/></svg>Payment<br>Posting</li>
    <li><svg class="tick"><use href="#tick"/></svg>Credentialing</li>
  </ul>
  <ul class="services services--b">
    <li><svg class="tick"><use href="#tick"/></svg>Comprehensive<br>Monthly Reports</li>
    <li><svg class="tick"><use href="#tick"/></svg>Denial Management<br>Including Appeals</li>
    <li><svg class="tick"><use href="#tick"/></svg>Past Due<br>Claims</li>
    <li><svg class="tick"><use href="#tick"/></svg>Insurance<br>Verification</li>
    <li><svg class="tick"><use href="#tick"/></svg>Claim Correction and<br>Resubmission</li>
  </ul>
  <ul class="services services--c">
    <li><svg class="tick"><use href="#tick"/></svg>Authorization<br>Tracking</li>
    <li><svg class="tick"><use href="#tick"/></svg>Practice<br>Consulting</li>
    <li><svg class="tick"><use href="#tick"/></svg>Remote Access<br>Consulting</li>
    <li><svg class="tick"><use href="#tick"/></svg>Tracking and Verifying<br>Allowables</li>
    <li><svg class="tick"><use href="#tick"/></svg>Emergency &ldquo;Fill In&rdquo; or<br>Transition Billing - Let<br>Us Work When You Can't</li>
  </ul>
  <span class="fold" style="left:237px"></span>
  <span class="fold" style="left:474px"></span>
</section>

</body>
</html>
```